CBD Boutique Business Card Needed

We are in need of a business card to reflect the direction of our latest products. We are a fully organic company in which our store and products are very heavy in wood and "natural" components. We decided to bring color into one of our brands and immediately knew this is where we needed to go.

We are NOT a cash grab CBD company. We could have done this wrong, slapped a label on a shit product and left it like that. I am passionate about sharing my experience with other veterans and opening a store and making it a comfortable place for others to come and see if they can have the same experience.

Target Market(s)

We are a dual market company. We do have a beauty line that will cover the costs of the majority of our business. But we also heavily cater to veterans and first responders. I am a veteran and this is how I found out about CBD. So the marketing needs to bring in our higher end beauty clientele but also be able to not put off our customers that readily need this.

Contact Information for Business Card

What we are looking for is a light, professional, boutique design that is is neither quite feminine or masculine. Attached is a picture of a store in Portland that we asked our store designer to get her inspiration from. But all natural wood and black outlines are what is mostly in there.

Attached are the following files:

Logo: An AI file with how we have our logo. I do not understand AI and have no idea why the letters are individual. The font is Adam. OLU is the logo and Tonics of Vigor is our tagline.

KM Vantage (front and back) cards I did originally found at a trade show that I absolutely loved...while it is mostly there and I would still be happy with them but it is me pretending to be you. I understand I am not and there is probably a lot wrong that all of you would see instantly and this is why I am here.

Dropper Bottle: This is our final product mock up

Water Color: I am semi flexible here. This water color is slightly different on every level of our brand. The color itself can change...we are not stuck on THIS particular one. If you happen to make a new one that is similar in style and we use it...then I will happily commission you to change the rest on our next product run. I am pretty sure you can use this statement as evidence later . =) .

But seriously, we heavily believe in pay it forward and will work with anyone here that may have a vision bigger than ours. The winner of this contest will get preferential consideration on our marketing materials (need letterhead etc. next, as well as a brochure, and website) so three more projects coming down the pipeline.

Information to use for your mockup is contained on the card images I have included. I would prefer CBD for wellness CBD for life to be more prominent. No where else on the card do we have CBD mentioned.

Font styles to use
Sans Serif

Colors

Designer to choose colors to be used in the design.

Requirements
Must have
• Double Sided
• Front: OLU logo on front of card will be raised embossed. Background is watercolor. One has been provided. Others are up for consideration. If the rest of your design is incredible and I don't like your watercolor I will just ask to swap it.
• Back: Standard information. Not stuck on anything here. I LOVE clean minimal designs. The bleed on the card I provided is a luxury...
• Font for title and OLU is Adam. Everything else I prefer san serif or as clean as possible.
Nice to have
• I Need to incorporate Naturally Nurturing somewhere on the card. Bold but not intrusive.

```html
<!DOCTYPE html>
<html lang="en">
<head>
<meta charset="utf-8">
<title>OLU — Business Card</title>
<link href="https://fonts.googleapis.com/css2?family=Arimo:wght@400&family=Montserrat:wght@300;400&display=swap" rel="stylesheet">
<style>
  :root {
    --stage: #2b2b2b;
    --paper: #ffffff;
    --ink: #1d1d1d;
    --ink-soft: #2e2e2e;
    --emboss: #d6d6d6;
    --mark-dark: #3f3f42;
    --wash-cool: #bfe0e2;
    --wash-warm: #efc79c;
  }
  * { margin: 0; padding: 0; box-sizing: border-box; }
  html, body {
    width: 1200px; height: 900px; overflow: hidden;
    background: var(--stage);
  }
  .stage { position: relative; width: 1200px; height: 900px; }
  .card {
    position: absolute; top: 144px;
    width: 403px; height: 611px;
    background: var(--paper);
    overflow: hidden;
  }
  .card--info { left: 167px; }
  .card--cover { left: 665px; }

  .wordmark {
    position: absolute; left: 0; right: 0;
    text-align: center;
    font-family: "Montserrat", sans-serif;
    font-weight: 300;
  }
  .wordmark__name {
    display: block;
    font-size: 112px; line-height: 1;
    letter-spacing: 14px;
    padding-left: 14px;
  }
  .wordmark__tagline {
    display: block;
    margin-top: 10px;
    font-size: 22px;
    letter-spacing: 3px;
    text-transform: uppercase;
  }
  .card--info .wordmark { top: 80px; color: var(--emboss); }
  .card--cover .wordmark { top: 246px; color: var(--mark-dark); }
  .card--cover .wordmark__name { font-size: 94px; letter-spacing: 12px; padding-left: 12px; }
  .card--cover .wordmark__tagline { font-size: 18px; margin-top: 4px; }

  .contact {
    position: absolute; left: 36px; top: 290px; right: 30px;
    font-family: "Montserrat", sans-serif;
    font-weight: 400;
    color: var(--ink-soft);
  }
  .contact__name {
    font-family: "Arimo", sans-serif;
    font-weight: 400;
    font-size: 25px; color: var(--ink);
    line-height: 1.2;
  }
  .contact__role {
    margin-top: 10px;
    font-size: 16px; letter-spacing: 0.6px;
    text-transform: uppercase;
  }
  .rule {
    width: 14px; height: 2px;
    background: var(--ink);
  }
  .rule--first { margin-top: 16px; }
  .contact__address {
    margin-top: 20px;
    font-size: 14.5px; line-height: 18px;
  }
  .rule--second { margin-top: 22px; }
  .channels { list-style: none; margin-top: 26px; }
  .channels li {
    display: flex; align-items: center;
    font-size: 14.5px; height: 27px;
  }
  .channels svg { width: 14px; height: 14px; margin-right: 9px; flex: none; }
  .slogan {
    margin-top: 13px;
    font-size: 14.5px;
    word-spacing: 1px;
  }

  .wash {
    position: absolute; inset: 0;
    background: linear-gradient(180deg, var(--wash-cool) 0%, var(--wash-warm) 100%);
  }
</style>
</head>
<body>
<main class="stage">

  <section class="card card--info">
    <div class="wordmark">
      <span class="wordmark__name">OLU</span>
      <span class="wordmark__tagline">Tonics of Vigor</span>
    </div>

    <div class="contact">
      <h1 class="contact__name">Dana Whitfield</h1>
      <p class="contact__role">Owner / CEO</p>
      <div class="rule rule--first"></div>
      <p class="contact__address">2140 N Cedar Hollow Rd Mesa,<br>AZ 85201 Suite 300</p>
      <div class="rule rule--second"></div>
      <ul class="channels">
        <li>
          <svg viewBox="0 0 16 16" fill="none" stroke="#2e2e2e" stroke-width="1.1" aria-hidden="true">
            <path d="M3.2 1.5l2.4 0 1 3.2-1.5 1.2c.8 1.8 2.2 3.2 4 4l1.2-1.5 3.2 1v2.4c0 .8-.7 1.5-1.5 1.5C6.6 13.3 2.7 9.4 1.7 3c0-.8.7-1.5 1.5-1.5z"/>
          </svg>
          555.014.2290
        </li>
        <li>
          <svg viewBox="0 0 16 16" fill="none" stroke="#2e2e2e" stroke-width="1.1" aria-hidden="true">
            <rect x="1" y="3" width="14" height="10"/>
            <path d="M1 3l7 6 7-6M1 13l5-5M15 13l-5-5"/>
          </svg>
          hello@olu.life
        </li>
        <li>
          <svg viewBox="0 0 16 16" fill="none" stroke="#2e2e2e" stroke-width="1.1" aria-hidden="true">
            <circle cx="8" cy="8" r="6.5"/>
            <ellipse cx="8" cy="8" rx="3" ry="6.5"/>
            <path d="M1.5 8h13M2.5 4.8h11M2.5 11.2h11"/>
          </svg>
          www.olu.life
        </li>
      </ul>
      <p class="slogan">CBD for wellness&nbsp; CBD for life</p>
    </div>
  </section>

  <section class="card card--cover">
    <div class="wash" role="img" aria-label="Placeholder for the watercolor wash artwork in teal and orange tones"></div>
    <div class="wordmark">
      <span class="wordmark__name">OLU</span>
      <span class="wordmark__tagline">Tonics of Vigor</span>
    </div>
  </section>

</main>
</body>
</html>
```